Real Estate Agent needs business card design

We have logo designed already, want to have business card designed. Very interested in those smaller size business card as they look very trendy. Business name is called VORENDA REALTY

```html
<!DOCTYPE html>
<html lang="en">
<head>
<meta charset="utf-8">
<title>Vorenda Realty – Business Card</title>
<link rel="stylesheet" href="https://fonts.googleapis.com/css2?family=Tinos:wght@400&family=Montserrat:wght@400&display=swap">
<style>
  :root {
    --gold: #c9a267;
    --gold-light: #d4b17f;
    --gold-deep: #c8a068;
    --ink: #1e1e1e;
    --text: #3a3a3a;
    --charcoal: #3b3b3b;
    --paper: #ffffff;
  }
  * { margin: 0; padding: 0; box-sizing: border-box; }
  html, body {
    width: 1200px; height: 840px; overflow: hidden;
    background: var(--paper);
  }
  .canvas { position: relative; width: 1200px; height: 840px; }

  .card {
    position: absolute; top: 206px;
    width: 429px; height: 428px;
    border-radius: 13px; overflow: hidden;
  }
  .card--front { left: 159px; background: var(--paper); border: 1px solid #ececec; }
  .card--back {
    left: 609px;
    background: linear-gradient(160deg, var(--gold-light) 0%, var(--gold-deep) 100%);
  }

  .brand-name {
    font-family: "Tinos", serif;
    font-variant: small-caps;
    font-weight: 400;
    letter-spacing: 0.5px;
    white-space: nowrap;
  }
  .brand-mark { position: absolute; width: 14px; height: 14px; }

  /* front */
  .card--front .brand-mark { right: 34px; top: 88px; background: var(--gold); }
  .card--front .brand-name {
    position: absolute; right: 34px; top: 108px;
    font-size: 34px; color: var(--ink); line-height: 1;
  }
  .holder-name {
    position: absolute; left: 36px; top: 276px;
    font-family: "Tinos", serif; font-size: 22px; letter-spacing: 0.6px;
    color: var(--gold);
  }
  .holder-role {
    position: absolute; left: 36px; top: 302px;
    font-family: "Tinos", serif; font-size: 15px; color: var(--ink);
  }
  .holder-rule {
    position: absolute; left: 102px; top: 313px;
    width: 293px; height: 1.5px; background: var(--gold);
  }
  .contact-list {
    position: absolute; left: 36px; top: 335px;
    list-style: none;
    font-family: "Montserrat", sans-serif; font-size: 13px; color: var(--text);
  }
  .contact-list li { display: flex; align-items: center; height: 18px; }
  .contact-list svg { width: 10px; height: 10px; margin-right: 9px; flex: none; }
  .address {
    position: absolute; right: 34px; top: 353px; text-align: right;
    font-family: "Montserrat", sans-serif; font-size: 13px; line-height: 16px;
    color: var(--text);
  }
  .footer-band { position: absolute; left: 0; bottom: 0; width: 429px; height: 14px; }

  /* back */
  .card--back .brand-mark { left: 207px; top: 196px; background: var(--paper); }
  .card--back .brand-name {
    position: absolute; left: 0; right: 0; top: 226px; text-align: center;
    font-size: 38px; color: var(--paper); line-height: 1;
  }
  .back-url {
    position: absolute; left: 0; right: 0; top: 379px; text-align: center;
    font-family: "Montserrat", sans-serif; font-size: 13px; color: var(--paper);
    letter-spacing: 0.3px;
  }
</style>
</head>
<body>
<main class="canvas">

  <section class="card card--front" aria-label="Card front">
    <span class="brand-mark" aria-hidden="true"></span>
    <p class="brand-name">Vorenda Realty</p>

    <p class="holder-name">Celine Marlow</p>
    <p class="holder-role">Founder</p>
    <span class="holder-rule" aria-hidden="true"></span>

    <ul class="contact-list">
      <li>
        <svg viewBox="0 0 10 10" aria-hidden="true"><rect x="2.5" y="0.5" width="5" height="9" rx="1" fill="none" stroke="var(--gold)" stroke-width="1"/><rect x="4.2" y="7.6" width="1.6" height="0.8" fill="var(--gold)"/></svg>
        (000)555-0142
      </li>
      <li>
        <svg viewBox="0 0 10 10" aria-hidden="true"><rect x="0.5" y="2" width="9" height="6.5" fill="var(--gold)"/><path d="M0.5 2 L5 5.6 L9.5 2" fill="none" stroke="#fff" stroke-width="0.9"/></svg>
        info@celinemarlow.com
      </li>
      <li>
        <svg viewBox="0 0 10 10" aria-hidden="true"><g fill="none" stroke="var(--gold)" stroke-width="0.9"><circle cx="5" cy="5" r="4.3"/><ellipse cx="5" cy="5" rx="1.9" ry="4.3"/><path d="M0.7 5 H9.3 M1.5 2.8 H8.5 M1.5 7.2 H8.5"/></g></svg>
        www.vorendarealty.com
      </li>
    </ul>

    <p class="address">48 Linden Court<br>Ashford, TN 37190</p>

    <svg class="footer-band" viewBox="0 0 429 14" preserveAspectRatio="none" aria-hidden="true">
      <polygon points="0,0 293,0 286,14 0,14" fill="var(--gold)"/>
      <polygon points="300,0 429,0 429,14 293,14" fill="var(--charcoal)"/>
    </svg>
  </section>

  <section class="card card--back" aria-label="Card back">
    <span class="brand-mark" aria-hidden="true"></span>
    <p class="brand-name">Vorenda Realty</p>
    <p class="back-url">www.vorendarealty.com</p>
  </section>

</main>
</body>
</html>
```